Orlenby

I'm starting my own CBD Company in the UK and wanting to have a very modern looking label for my CBD tincture bottles. I am starting off with two types of strengths of CBD. For each strength percentage i'm wanting a different Colour on the label. I'm wanting the design to look very similar to these products and the organic pastel colours that are on this company's labels, I really like there design! (https://valoreth.com/). My two strengths are 4% & 15%. Can you please provide more than two colour examples. I want my logo horizontal. Please find my logo and a few examples that have been attached.

```html
<!DOCTYPE html>
<html lang="en">
<head>
<meta charset="utf-8">
<title>Orlenby – Hemp Drops Labels</title>
<link rel="stylesheet" href="https://fonts.googleapis.com/css2?family=Playfair+Display:wght@600&family=Poppins:wght@600&display=swap">
<style>
  :root {
    --backdrop: #8289a5;
    --label-bg: #ffffff;
    --label-edge: #3d3d48;
    --ink: #58566e;
    --ink-dark: #4a4a55;
    --tan: #dfc194;
    --sage: #c9cf9b;
    --white: #ffffff;
  }
  * { margin: 0; padding: 0; box-sizing: border-box; }
  html, body { width: 1200px; height: 1170px; overflow: hidden; }
  body { background: var(--backdrop); position: relative; }

  .label {
    position: absolute;
    left: 43px;
    width: 1114px;
    height: 519px;
    background: var(--label-bg);
    border: 1px solid var(--label-edge);
    overflow: hidden;
  }
  .label--strong { top: 37px; --accent: var(--tan); }
  .label--mild { top: 589px; --accent: var(--sage); }

  .brand-name {
    position: absolute;
    top: 70px;
    left: 0; right: 0;
    height: 90px;
    line-height: 90px;
    text-align: center;
    font-family: 'Playfair Display', serif;
    font-weight: 600;
    font-size: 64px;
    color: var(--ink);
  }

  .accent-line {
    position: absolute;
    left: 0; right: 0;
    top: 198px;
    height: 10px;
    background: var(--accent);
  }
  .accent-band {
    position: absolute;
    left: 0; right: 0;
    top: 216px;
    height: 148px;
    background: var(--accent);
  }
  .ribbon {
    position: absolute;
    left: 509px;
    top: 212px;
    width: 108px;
    height: 137px;
  }
  .ribbon svg { display: block; width: 100%; height: 100%; }
  .strength {
    position: absolute;
    left: 0; right: 0;
    top: 10px;
    text-align: center;
    font-family: 'Playfair Display', serif;
    font-weight: 600;
    font-size: 50px;
    line-height: 0.95;
    font-variant-numeric: lining-nums;
    color: var(--accent);
  }
  .strength-sign { font-size: 46px; }

  .product-name {
    position: absolute;
    left: 0; right: 0;
    top: 364px;
    height: 40px;
    line-height: 40px;
    text-align: center;
    font-family: 'Playfair Display', serif;
    font-weight: 600;
    font-size: 32px;
    letter-spacing: 1px;
    color: var(--ink-dark);
  }
  .dose-band {
    position: absolute;
    left: 0; right: 0;
    top: 404px;
    height: 44px;
    line-height: 44px;
    background: var(--accent);
    text-align: center;
    font-family: 'Poppins', sans-serif;
    font-weight: 600;
    font-size: 26px;
    color: var(--white);
  }
</style>
</head>
<body>

<section class="label label--strong">
  <div class="brand-name">Orlenby</div>
  <div class="accent-line"></div>
  <div class="accent-band"></div>
  <div class="ribbon">
    <svg viewBox="0 0 108 137" aria-hidden="true"><polygon points="0,0 108,0 108,137 54,119 0,137" fill="#ffffff"/></svg>
    <div class="strength">15<br><span class="strength-sign">%</span></div>
  </div>
  <div class="product-name">HEMP DROPS</div>
  <div class="dose-band">400mg CBD</div>
</section>

<section class="label label--mild">
  <div class="brand-name">Orlenby</div>
  <div class="accent-line"></div>
  <div class="accent-band"></div>
  <div class="ribbon">
    <svg viewBox="0 0 108 137" aria-hidden="true"><polygon points="0,0 108,0 108,137 54,119 0,137" fill="#ffffff"/></svg>
    <div class="strength">4<br><span class="strength-sign">%</span></div>
  </div>
  <div class="product-name">HEMP DROPS</div>
  <div class="dose-band">400mg CBD</div>
</section>

</body>
</html>
```